Corinne Dabney Interiors business cards

We need a DOUBLE SIDED business card design that is simple, elegant and modern. We are a rapidly growing Interior Design Firm, and our brand colours are blush pink, navy, and antique gold, so we require some or all of these colours to be used. The final design should portray elegance, simplicity, and have a modern feel. We have upload inspiration photos that have the feel we're looking for.

Industry/Entity Type

Interior Design

Contact Information for Business Card

Contact information and LOGO

Colors
EB3D1F
EC4F4E
F09395
F8D3D4
FCEDEE

Requirements
Must have
• Navy, the right shade of blush pink, and antique gold

```html
<!DOCTYPE html>
<html lang="en">
<head>
<meta charset="utf-8">
<title>Corinne Dabney Interiors – Business Cards</title>
<link href="https://fonts.googleapis.com/css2?family=Montserrat:wght@400;500;600&display=swap" rel="stylesheet">
<style>
  :root {
    --backdrop: #b3b3b3;
    --navy: #2e3b53;
    --blush: #e8c5b8;
    --white: #ffffff;
    --gold-dark: #d4ad66;
    --gold-light: #f0cf8c;
  }
  * { margin: 0; padding: 0; box-sizing: border-box; }
  html, body { width: 1000px; height: 1200px; overflow: hidden; background: var(--backdrop); }
  body { position: relative; font-family: "Montserrat", sans-serif; }

  .card { position: absolute; left: 50px; width: 900px; height: 540px; overflow: hidden; }
  .card--front { top: 43px; background: var(--white); }
  .card--back { top: 617px; background: var(--navy); }
  .card__shapes { position: absolute; inset: 0; width: 900px; height: 540px; }

  .brand { position: absolute; text-align: center; font-weight: 400; line-height: 1; }
  .brand__square { position: absolute; }
  .brand__name { position: absolute; white-space: nowrap; transform: translateX(-50%); }
  .brand__line1 { font-size: 36px; letter-spacing: -0.5px; }
  .brand__line2 { font-size: 22px; letter-spacing: 12px; margin-top: 12px; padding-left: 12px; }

  .card--front .brand__square { left: 195px; top: 148px; width: 152px; height: 152px; background: var(--navy); }
  .card--front .brand__name { left: 270px; top: 335px; color: var(--navy); }
  .card--back .brand__square { left: 69px; top: 384px; width: 102px; height: 102px; background: var(--white); }
  .card--back .brand__name { left: 381px; top: 410px; color: var(--white); }
  .card--back .brand__line1 { font-size: 34px; }
  .card--back .brand__line2 { font-size: 20px; margin-top: 10px; }

  .contact { position: absolute; left: 572px; top: 46px; color: var(--navy); }
  .contact__name { font-size: 27px; font-weight: 600; line-height: 30px; }
  .contact__role { font-size: 23px; font-weight: 400; line-height: 32px; margin-bottom: 10px; }
  .contact__list { list-style: none; }
  .contact__item { display: flex; align-items: center; height: 38px; font-size: 22px; font-weight: 400; }
  .contact__icon { width: 23px; height: 23px; margin-right: 9px; flex: none; }
</style>
</head>
<body>
  <defs-holder hidden></defs-holder>

  <section class="card card--front" aria-label="Card front">
    <svg class="card__shapes" viewBox="0 0 900 540" aria-hidden="true">
      <defs>
        <linearGradient id="goldFront" x1="0" y1="1" x2="1" y2="0.3">
          <stop offset="0" stop-color="var(--gold-dark)"/>
          <stop offset="0.6" stop-color="var(--gold-light)"/>
          <stop offset="1" stop-color="var(--gold-dark)"/>
        </linearGradient>
      </defs>
      <polygon points="288,0 900,0 900,247 564,452" fill="var(--blush)"/>
      <polygon points="0,540 206,415 283,540" fill="url(#goldFront)"/>
    </svg>

    <div class="brand">
      <div class="brand__square"></div>
      <div class="brand__name">
        <div class="brand__line1">CORINNE DABNEY</div>
        <div class="brand__line2">INTERIORS</div>
      </div>
    </div>

    <div class="contact">
      <div class="contact__name">Your Name</div>
      <div class="contact__role">Manager</div>
      <ul class="contact__list">
        <li class="contact__item">
          <svg class="contact__icon" viewBox="0 0 24 24" aria-hidden="true"><rect width="24" height="24" rx="3" fill="var(--navy)"/><path d="M8 5.5l2.2 2.6-1.2 1.6c.8 1.8 2.3 3.3 4.1 4.1l1.6-1.2 2.6 2.2-1.3 2.2c-4.8-.6-9-4.8-9.6-9.6z" fill="var(--white)"/></svg>
          123 444 555
        </li>
        <li class="contact__item">
          <svg class="contact__icon" viewBox="0 0 24 24" aria-hidden="true"><rect width="24" height="24" rx="3" fill="var(--navy)"/><path d="M12 4a4.5 4.5 0 0 0-4.5 4.5c0 3.2 4.5 8 4.5 8s4.5-4.8 4.5-8A4.5 4.5 0 0 0 12 4zm0 6.3a1.8 1.8 0 1 1 0-3.6 1.8 1.8 0 0 1 0 3.6z" fill="var(--white)"/><rect x="7" y="18" width="10" height="1.6" fill="var(--white)"/></svg>
          789 Your Street Here
        </li>
        <li class="contact__item">
          <svg class="contact__icon" viewBox="0 0 24 24" aria-hidden="true"><rect width="24" height="24" rx="3" fill="var(--navy)"/><rect x="5" y="7" width="14" height="10" fill="none" stroke="var(--white)" stroke-width="1.5"/><path d="M5 7l7 6 7-6M5 17l5-5M19 17l-5-5" fill="none" stroke="var(--white)" stroke-width="1.3"/></svg>
          info@yourname.com
        </li>
        <li class="contact__item">
          <svg class="contact__icon" viewBox="0 0 24 24" aria-hidden="true"><rect width="24" height="24" rx="3" fill="var(--navy)"/><g fill="none" stroke="var(--white)" stroke-width="1.3"><circle cx="12" cy="12" r="6.5"/><ellipse cx="12" cy="12" rx="2.8" ry="6.5"/><path d="M5.5 12h13M6.5 8.8h11M6.5 15.2h11"/></g></svg>
          www.yourname.com
        </li>
      </ul>
    </div>
  </section>

  <section class="card card--back" aria-label="Card back">
    <svg class="card__shapes" viewBox="0 0 900 540" aria-hidden="true">
      <defs>
        <linearGradient id="goldBack" x1="0" y1="0.3" x2="1" y2="1">
          <stop offset="0" stop-color="var(--gold-dark)"/>
          <stop offset="0.4" stop-color="var(--gold-light)"/>
          <stop offset="1" stop-color="var(--gold-dark)"/>
        </linearGradient>
      </defs>
      <polygon points="0,0 478,0 262,352 0,192" fill="var(--blush)"/>
      <polygon points="618,540 694,414 900,540" fill="url(#goldBack)"/>
    </svg>

    <div class="brand">
      <div class="brand__square"></div>
      <div class="brand__name">
        <div class="brand__line1">CORINNE DABNEY</div>
        <div class="brand__line2">INTERIORS</div>
      </div>
    </div>
  </section>
</body>
</html>
```